New App Design Project

We are having an app built and require the following:

App Icons
120x120 - iphone/ipod touch - HD
76x76 - Tabby
152x152 - Tabby - HD

AppStore Icon
1024x1024 PNG

Launch Screen
320x480 - iphone/ipod touch
640x960 - iPhone/iPod touch - HD
768x1004 - Tabby (Portrait)
1024x748 - Tabby (Landscape)
1536x2008 - Tabby (Portrait) = HD
2048x1496 - Tabby (Landscape) -HD

ALSO NEED

WELCOME PAGE AND CONTACT US PAGE - STATIC WITH CLICKABLE LINKS for an example of what we want please view the uPage app in the quillbox store.

Text for use in the welcome screen

Welcome to the Marrowby EBook App

The Marrowby App allows you to easily read and navigate monthly updated Ebooks.

From the comfort of you mobile device you can electronically flip through our latest listings from both For Sale and Rental Properties.

Visit our Ebooks:

Residential Properties FOR SALE

Residential Properties suited for INVESTORS

Residential Properties FOR RENT

 

A little about Marrowby…

When you list your property exclusively with Marrowby, we guarantee to advertise it totally free of charge – whether it is sold or withdrawn from the market.

We call it the Marrowby Keystone Marketing Strategy. It’s an approach we’ve researched and designed to generate as many enquiries as possible.

We stand by our reputation for providing a superior service and delivering results – across six offices, seven days a week.

That’s why a third of all property sellers on the northern Gold Coast choose Marrowby as their exclusive agent.

With the wide reaching effects of the Marrowby Keystone Marketing Strategy and over 40 sales people working together to sell your property, you’ll be making the right move with Marrowby.

Industry/Entity Type

Landscape

Requirements
Must have
• Our company logo

```html
<!DOCTYPE html>
<html lang="en">
<head>
<meta charset="utf-8">
<title>Marrowby EBook App – Contact Us</title>
<link rel="stylesheet" href="https://fonts.googleapis.com/css2?family=Fira+Sans:wght@600&family=Source+Sans+3:wght@400&display=swap">
<style>
  :root {
    --red-core: #dc262c;
    --red-mid: #b8161c;
    --red-edge: #7e0c11;
    --white: #ffffff;
    --paper: #ffffff;
    --ink: #1f1f1f;
    --rule-glow: rgba(255, 140, 140, 0.75);
  }
  * { margin: 0; padding: 0; box-sizing: border-box; }
  html, body {
    width: 1200px;
    height: 1092px;
    overflow: hidden;
    background: var(--paper);
  }
  .screen {
    position: relative;
    width: 1200px;
    height: 1092px;
  }
  .splash {
    position: absolute;
    left: 0; top: 0;
    width: 1200px;
    height: 894px;
    background: radial-gradient(ellipse 720px 560px at 600px 430px,
      var(--red-core) 0%, var(--red-mid) 50%, var(--red-edge) 100%);
    color: var(--white);
    font-family: "Source Sans 3", sans-serif;
  }
  .brand-square {
    position: absolute;
    left: 120px; top: 180px;
    width: 306px; height: 306px;
    background: var(--white);
  }
  .brand-name {
    position: absolute;
    left: 456px; top: 132px;
    font-size: 158px;
    line-height: 1;
    font-weight: 400;
    letter-spacing: -1px;
  }
  .brand-product {
    position: absolute;
    left: 462px; top: 320px;
    font-size: 134px;
    line-height: 1;
    font-weight: 400;
  }
  .rule {
    position: absolute;
    left: 90px;
    width: 1020px;
    height: 3px;
    background: linear-gradient(90deg, transparent, var(--rule-glow) 25%, var(--rule-glow) 75%, transparent);
  }
  .rule-top { top: 540px; }
  .rule-bottom { top: 786px; }
  .page-title {
    position: absolute;
    left: 0; top: 580px;
    width: 1200px;
    text-align: center;
    font-size: 140px;
    line-height: 1;
    font-weight: 400;
    letter-spacing: 2px;
  }
  .format-label {
    position: absolute;
    left: 0; top: 935px;
    width: 1200px;
    text-align: center;
    font-family: "Fira Sans", sans-serif;
    font-weight: 600;
    font-size: 90px;
    line-height: 1;
    color: var(--ink);
  }
</style>
</head>
<body>
  <main class="screen">
    <section class="splash">
      <div class="brand-square" aria-hidden="true"></div>
      <div class="brand-name">Marrowby</div>
      <div class="brand-product">EBook App</div>
      <div class="rule rule-top"></div>
      <h1 class="page-title">CONTACT US</h1>
      <div class="rule rule-bottom"></div>
    </section>
    <p class="format-label">Tabby HD Portrait</p>
  </main>
</body>
</html>
```